TalkBridge - Language Coaching Services

Sleek, innovative, trendy design for Language Coaching business.

TalkBridge is a new UK based company that provides Language Coaching services. We offer highly personalized on-line and face to face language courses. We also impart learning techniques workshops based on the latest neuroscience research for second-language acquisition.

Target Market(s)

Industry/Entity Type

Consulting

Contact Information for Business Card

TalkBridge
ElenaVT@talkbridge-demo.co.uk
TalkBridge-demo.co.uk
London, UK

Font styles to use
Sans Serif

```html
<!DOCTYPE html>
<html lang="en">
<head>
<meta charset="utf-8">
<title>TalkBridge – Business Card</title>
<link rel="stylesheet" href="https://fonts.googleapis.com/css2?family=Open+Sans:wght@400;600;700&display=swap">
<style>
  :root {
    --bg-top: #f1f1f2;
    --bg-bottom: #cfcfd2;
    --card-dark: #2b3034;
    --card-light: #ffffff;
    --brand-blue: #3a8fc9;
    --brand-navy: #3d6894;
    --ink: #1f2226;
    --ink-soft: #3b3f44;
  }
  * { margin: 0; padding: 0; box-sizing: border-box; }
  html, body { width: 1200px; height: 900px; overflow: hidden; }
  body {
    background: linear-gradient(180deg, var(--bg-top), var(--bg-bottom));
    font-family: "Open Sans", Arial, sans-serif;
    position: relative;
  }
  .card {
    position: absolute;
    width: 540px;
    height: 309px;
    border-radius: 2px;
    box-shadow: 0 10px 24px rgba(0,0,0,.18);
  }
  .card--front { left: 30px; top: 250px; background: var(--card-dark); }
  .card--back  { left: 630px; top: 250px; background: var(--card-light); }

  .brand {
    display: flex;
    flex-direction: column;
    align-items: center;
    gap: 14px;
  }
  .brand__circle {
    border-radius: 50%;
    border-style: solid;
  }
  .brand__name {
    font-weight: 600;
    letter-spacing: 2px;
    text-transform: uppercase;
    line-height: 1;
  }

  .card--front .brand {
    position: absolute; left: 0; right: 0; top: 70px;
  }
  .card--front .brand__circle { width: 100px; height: 100px; border-width: 6px; border-color: var(--brand-blue); }
  .card--front .brand__name { font-size: 40px; color: var(--brand-blue); }

  .card--back .brand {
    position: absolute; left: 36px; top: 110px; align-items: flex-start;
  }
  .card--back .brand__circle { width: 66px; height: 66px; border-width: 4px; border-color: var(--brand-navy); margin-left: 60px; }
  .card--back .brand__name { font-size: 26px; color: var(--brand-navy); }

  .holder {
    position: absolute; right: 30px; top: 34px; text-align: right;
  }
  .holder__name { font-size: 13px; font-weight: 700; color: var(--ink); letter-spacing: .5px; text-transform: uppercase; }
  .holder__role { font-size: 9px; color: var(--ink-soft); }

  .contacts {
    position: absolute; left: 300px; top: 118px; list-style: none;
    display: flex; flex-direction: column; gap: 9px;
  }
  .contacts__item {
    display: flex; align-items: flex-start; gap: 9px;
    font-size: 10px; color: var(--ink-soft); line-height: 14px;
  }
  .contacts__icon {
    flex: none; width: 14px; height: 14px; border-radius: 50%;
    background: var(--brand-navy);
    display: flex; align-items: center; justify-content: center;
  }
  .contacts__icon svg { width: 8px; height: 8px; }

  .presentation-mark {
    position: absolute; right: 52px; bottom: 40px;
  }
  .presentation-mark .brand__circle { width: 78px; height: 78px; border-width: 5px; border-color: var(--brand-blue); }
  .presentation-mark .brand__name { font-size: 28px; color: var(--brand-blue); }
</style>
</head>
<body>

  <section class="card card--front" aria-label="Card front">
    <div class="brand">
      <span class="brand__circle"></span>
      <span class="brand__name">TalkBridge</span>
    </div>
  </section>

  <section class="card card--back" aria-label="Card back">
    <div class="brand">
      <span class="brand__circle"></span>
      <span class="brand__name">TalkBridge</span>
    </div>

    <div class="holder">
      <p class="holder__name">Elena Torres</p>
      <p class="holder__role">Co-Founder</p>
    </div>

    <ul class="contacts">
      <li class="contacts__item">
        <span class="contacts__icon">
          <svg viewBox="0 0 10 10"><path d="M2 1 L4 1 L4.5 3 L3.5 4 Q4.5 6 6 6.5 L7 5.5 L9 6 L9 8 Q9 9 8 9 Q1 8.5 1 2 Q1 1 2 1 Z" fill="#fff"/></svg>
        </span>
        (020) 555 0148
      </li>
      <li class="contacts__item">
        <span class="contacts__icon">
          <svg viewBox="0 0 10 10"><rect x="1" y="2.2" width="8" height="5.6" fill="#fff"/><path d="M1 2.2 L5 5.5 L9 2.2" stroke="#3d6894" stroke-width="0.9" fill="none"/></svg>
        </span>
        hello@talkbridge-demo.co.uk
      </li>
      <li class="contacts__item">
        <span class="contacts__icon">
          <svg viewBox="0 0 10 10"><circle cx="5" cy="5" r="3.8" fill="none" stroke="#fff" stroke-width="1"/><ellipse cx="5" cy="5" rx="1.6" ry="3.8" fill="none" stroke="#fff" stroke-width="0.8"/><line x1="1.2" y1="5" x2="8.8" y2="5" stroke="#fff" stroke-width="0.8"/></svg>
        </span>
        www.talkbridge-demo.co.uk
      </li>
      <li class="contacts__item">
        <span class="contacts__icon">
          <svg viewBox="0 0 10 10"><path d="M5 9.5 Q1.5 5.5 1.5 4 A3.5 3.5 0 0 1 8.5 4 Q8.5 5.5 5 9.5 Z" fill="#fff"/><circle cx="5" cy="4" r="1.3" fill="#3d6894"/></svg>
        </span>
        <span>45 Harbour Lane, Suite 12<br>London EC1A 4XY, UK</span>
      </li>
    </ul>
  </section>

  <div class="brand presentation-mark">
    <span class="brand__circle"></span>
    <span class="brand__name">TalkBridge</span>
  </div>

</body>
</html>
```